Poster for Office

Looking for an edgy, beautiful poster to hang up in my office that uses the quotes located below and potentially the image attached.
Content for poster

Title: Pell's Rules

Must have the following quotes included (punctuation and capitalization are flexible, do what you think looks the best they also don't need the quotation symbols):

"Don't order fish at a steakhouse"
"Be bold. The more you tell, the more you sell"
"admit nothing, deny everything, launch counterattack."
"avoid obviousness"
"never do anything until you're ready to do it"
"look good=feel good"
"always keep the advantage"
"never complain, never explain"
"Lay low, play dumb, keep moving"

Industry/Entity Type

Quotes

Requirements
Must have
• Title: Pell's Rules

"avoid obviousness"
"look good=feel good"

```html
<!DOCTYPE html>
<html lang="en">
<head>
<meta charset="utf-8">
<title>Pell's Rules</title>
<link rel="stylesheet" href="https://fonts.googleapis.com/css2?family=Archivo+Black&family=Oswald:wght@600;700&family=Russo+One&display=swap">
<style>
  :root {
    --ink-dark: #1d2121;
    --photo-mid: #5f6262;
    --photo-light: #8a8c8b;
    --glow: rgba(255, 255, 255, 0.9);
    --blue-bright: #2f5ff2;
    --blue-soft: #5b7fe4;
    --blue-deep: #1631c9;
    --blue-sky: #7fb3ec;
    --blue-royal: #2a49d8;
    --blue-lilac: #6f7fe6;
    --blue-cyan: #58a6ea;
    --blue-mid: #3a6cf0;
    --blue-navy: #1b2fd2;
  }
  html, body {
    margin: 0;
    padding: 0;
    overflow: hidden;
    background: var(--ink-dark);
  }
  .poster {
    position: relative;
    width: 854px;
    height: 1200px;
    overflow: hidden;
    background: var(--ink-dark);
  }
  .poster__photo {
    position: absolute;
    inset: 0;
    background:
      radial-gradient(ellipse 380px 700px at 0% 60%, var(--photo-light), transparent 70%),
      radial-gradient(ellipse 380px 700px at 100% 60%, var(--photo-light), transparent 70%),
      linear-gradient(180deg, var(--ink-dark) 0%, var(--ink-dark) 18%, var(--photo-mid) 45%, var(--photo-mid) 100%);
  }
  .rules {
    position: absolute;
    inset: 0;
    margin: 0;
    padding: 0;
    list-style: none;
  }
  .rules__title,
  .rule {
    position: absolute;
    left: 0;
    right: 0;
    margin: 0;
    text-align: center;
    white-space: nowrap;
    line-height: 1;
    text-shadow: 0 0 6px var(--glow), 0 0 14px var(--glow);
  }
  .rules__title {
    top: 262px;
    font-family: "Archivo Black", sans-serif;
    font-size: 104px;
    color: var(--blue-bright);
    letter-spacing: -1px;
  }
  .rule--condensed { font-family: "Oswald", sans-serif; font-weight: 700; }
  .rule--wide { font-family: "Russo One", sans-serif; }

  .rule--fish    { top: 468px; font-size: 50px; color: var(--blue-bright); }
  .rule--bold    { top: 536px; font-size: 34px; color: var(--blue-soft); letter-spacing: 0.5px; }
  .rule--admit   { top: 592px; font-size: 27px; color: var(--blue-deep); font-weight: 600; }
  .rule--obvious { top: 630px; font-size: 66px; color: var(--blue-sky); letter-spacing: 3px; }
  .rule--ready   { top: 714px; font-size: 35px; color: var(--blue-royal); }
  .rule--look    { top: 770px; font-size: 54px; color: var(--blue-lilac); letter-spacing: 7px; }
  .rule--edge    { top: 838px; font-size: 33px; color: var(--blue-cyan); letter-spacing: 5px; }
  .rule--complain{ top: 890px; font-size: 44px; color: var(--blue-mid); }
  .rule--lay     { top: 958px; font-size: 35px; color: var(--blue-navy); letter-spacing: 2px; }
</style>
</head>
<body>
  <main class="poster">
    <div class="poster__photo" role="img" aria-label="Grayscale photo montage of two men seen from behind, shoulders and heads framing the text, with smaller portrait faces at the sides"></div>
    <h1 class="rules__title">Pell's Rules</h1>
    <ul class="rules">
      <li class="rule rule--condensed rule--fish">Don’t order fish at a steakhouse</li>
      <li class="rule rule--condensed rule--bold">Be bold. The more you tell, the more you sell</li>
      <li class="rule rule--condensed rule--admit">admit nothing, deny everything, launch counterattack</li>
      <li class="rule rule--wide rule--obvious">avoid obviousness</li>
      <li class="rule rule--condensed rule--ready">never do anything until you’re ready to do it</li>
      <li class="rule rule--wide rule--look">look good=feel good</li>
      <li class="rule rule--wide rule--edge">always keep the advantage</li>
      <li class="rule rule--wide rule--complain">never complain, never explain</li>
      <li class="rule rule--wide rule--lay">lay low, play dumb, keep moving</li>
    </ul>
  </main>
</body>
</html>
```